" Somos um escritório de contabilidade que quer quebrar o paradigma da contabilidade tradicional, focamos no atendimento personalizado e muita tecnologia para nos dar suporte na recepção e processamento das informações. "

```html
<!DOCTYPE html>
<html lang="pt-BR">
<head>
<meta charset="UTF-8">
<title>Numera — Papel timbrado</title>
<link rel="stylesheet" href="https://fonts.googleapis.com/css2?family=Open+Sans:wght@400;600&display=swap">
<style>
  :root {
    --backdrop: #e9e6e1;
    --paper: #ffffff;
    --ink: #4a4f55;
    --ink-soft: #7a7f86;
    --brand: #23566b;
    --teal: #2f8fa6;
    --red: #e2533d;
    --yellow: #f0c04a;
  }
  * { box-sizing: border-box; margin: 0; padding: 0; }
  html, body {
    width: 1200px; height: 1200px; overflow: hidden;
    background: var(--backdrop);
    font-family: "Open Sans", Arial, sans-serif;
  }
  .canvas {
    width: 1200px; height: 1200px;
    display: flex; align-items: center; justify-content: center;
  }
  .letterhead {
    position: relative;
    width: 800px; height: 1131px;
    background: var(--paper);
    box-shadow: 0 10px 30px rgba(0,0,0,0.12);
    padding: 80px 80px 0 80px;
  }
  .brand-name {
    display: block;
    font-weight: 600; font-size: 34px; line-height: 1.2;
    color: var(--brand);
    letter-spacing: 0.2px;
  }
  .letter-body {
    margin-top: 90px;
    font-size: 14px; line-height: 1.85; color: var(--ink);
  }
  .letter-body p { margin-bottom: 22px; text-align: justify; }
  .footer {
    position: absolute; left: 80px; right: 80px; bottom: 60px;
    display: grid; grid-template-columns: 1fr 1fr; gap: 12px 40px;
    font-size: 12px; color: var(--ink-soft);
  }
  .contact { display: flex; align-items: center; gap: 10px; white-space: nowrap; }
  .contact-icon { width: 18px; height: 18px; flex: none; }
  .color-bar {
    position: absolute; left: 0; right: 0; bottom: 0; height: 14px;
    display: flex;
  }
  .color-bar span { flex: 1; }
  .bar-teal { background: var(--teal); }
  .bar-red { background: var(--red); }
  .bar-yellow { background: var(--yellow); }
</style>
</head>
<body>
<div class="canvas">
  <article class="letterhead">
    <header class="brand">
      <span class="brand-name">Numera</span>
    </header>

    <section class="letter-body">
      <p>Prezado cliente, agradecemos a confiança em nosso trabalho. Nossa equipe acompanha cada etapa da sua rotina fiscal com atenção e clareza, usando ferramentas digitais que tornam o envio de documentos simples e rápido. Seguimos à disposição para esclarecer qualquer dúvida sobre obrigações, prazos e relatórios mensais.</p>
      <p>Informamos que o fechamento do período será concluído até o dia quinze. Pedimos que os extratos bancários e as notas emitidas sejam enviados pela plataforma, para que possamos processar tudo com segurança e entregar os balancetes no prazo combinado.</p>
      <p>Atenciosamente,</p>
    </section>

    <footer class="footer">
      <div class="contact">
        <svg class="contact-icon" viewBox="0 0 20 20" aria-hidden="true"><circle cx="10" cy="10" r="10" fill="#23566b"/><path d="M7 5.5l1.6 0 .8 2.4-1.1.8a6 6 0 0 0 3 3l.8-1.1 2.4.8v1.6c0 .6-.5 1-1 1A8 8 0 0 1 6 6.5c0-.5.4-1 1-1z" fill="#fff"/></svg>
        <span>(11) 4000-1234</span>
      </div>
      <div class="contact">
        <svg class="contact-icon" viewBox="0 0 20 20" aria-hidden="true"><circle cx="10" cy="10" r="10" fill="#23566b"/><circle cx="10" cy="10" r="5" fill="none" stroke="#fff" stroke-width="1.4"/><path d="M5 10h10M10 5v10" stroke="#fff" stroke-width="1"/></svg>
        <span>www.numera.com.br</span>
      </div>
      <div class="contact">
        <svg class="contact-icon" viewBox="0 0 20 20" aria-hidden="true"><circle cx="10" cy="10" r="10" fill="#23566b"/><rect x="5" y="6.5" width="10" height="7" fill="none" stroke="#fff" stroke-width="1.3"/><path d="M5 6.5l5 4 5-4" fill="none" stroke="#fff" stroke-width="1.3"/></svg>
        <span>ola@numera.com.br</span>
      </div>
      <div class="contact">
        <svg class="contact-icon" viewBox="0 0 20 20" aria-hidden="true"><circle cx="10" cy="10" r="10" fill="#23566b"/><path d="M10 4.5a3.5 3.5 0 0 0-3.5 3.5c0 2.6 3.5 7 3.5 7s3.5-4.4 3.5-7A3.5 3.5 0 0 0 10 4.5z" fill="#fff"/><circle cx="10" cy="8" r="1.3" fill="#23566b"/></svg>
        <span>Rua das Palmeiras, 120 · São Paulo, SP</span>
      </div>
    </footer>

    <div class="color-bar">
      <span class="bar-teal"></span>
      <span class="bar-red"></span>
      <span class="bar-yellow"></span>
    </div>
  </article>
</div>
</body>
</html>
```